Mental Health Awareness License Plates

Below is the sample format I will need. That of a plain license plate w/o frame
*refer to image with name Licence wo Frame*
Delete Frame
Replace QR Code with “MO”
Replace 2025 sticker with “ YR
Use License Plate font (attached)
On Ribbon, keep the green background
The California front leg, needs to be gradated like a sunset and retain shape of CA
Palm trees sharpened
I need the files in a format that can be used on a website, printed or made into a poster.
One file that reads SAMPLE, one version that reads “NEWPLA8”d
The finished product should look like a license plate as shown in the example
*refer to image name finished product*
I want to clarify what we are looking for. The license plate design has been approved by the state, but we need a high res version of it in multiple file formats. The most important change we are looking for is to the ribbon. The palm trees against the sunset are fuzzy, we need those placed in front of an sunset on the front leg of the ribbon. The rear leg needs to remain green (mental health color). I hope this help clarify our design need.

```html
<!DOCTYPE html>
<html lang="en">
<head>
<meta charset="utf-8">
<title>Mental Health Awareness License Plate</title>
<link rel="stylesheet" href="https://fonts.googleapis.com/css2?family=Saira+Condensed:wght@400&family=Titillium+Web:wght@600;700&display=swap">
<style>
  :root {
    --page-bg: #ececec;
    --plate-white: #f7f7f7;
    --plate-black: #231f20;
    --ink-dark: #231f20;
    --ink-light: #ffffff;
    --state-red: #e8474f;
    --tag-gold: #dfb42a;
    --ribbon-green: #2a9d48;
    --sunset-top: #f6c26b;
    --sunset-mid: #e9a27a;
    --sunset-low: #9fb37a;
  }
  html, body {
    margin: 0;
    padding: 0;
    width: 1200px;
    height: 770px;
    overflow: hidden;
    background: var(--page-bg);
  }
  .canvas {
    position: relative;
    width: 1200px;
    height: 770px;
  }
  .plate {
    position: absolute;
    left: 117px;
    top: 82px;
    width: 966px;
    height: 603px;
    background: var(--plate-white);
  }
  .plate-heading,
  .plate-footer {
    position: absolute;
    left: 0;
    width: 100%;
    text-align: center;
    font-family: "Titillium Web", sans-serif;
    font-weight: 700;
    color: var(--ink-dark);
    margin: 0;
    line-height: 1;
  }
  .plate-heading { top: 10px; font-size: 42px; }
  .plate-footer { bottom: 8px; font-size: 38px; letter-spacing: 0.5px; }
  .plate-field {
    position: absolute;
    left: 31px;
    top: 58px;
    width: 896px;
    height: 485px;
    background: var(--plate-black);
  }
  .tag {
    position: absolute;
    top: 30px;
    width: 132px;
    height: 75px;
    background: var(--tag-gold);
    color: var(--ink-dark);
    font-family: "Titillium Web", sans-serif;
    font-weight: 600;
    font-size: 38px;
    display: flex;
    align-items: center;
    justify-content: center;
  }
  .tag-month { left: 22px; }
  .tag-year { right: 22px; }
  .state-name {
    position: absolute;
    top: 20px;
    left: 0;
    width: 100%;
    text-align: center;
    font-family: "Titillium Web", sans-serif;
    font-weight: 600;
    font-size: 76px;
    color: var(--state-red);
    line-height: 1.1;
    margin: 0;
  }
  .mount-hole {
    position: absolute;
    left: 573px;
    top: 106px;
    width: 11px;
    height: 11px;
    border-radius: 50%;
    background: var(--ink-light);
  }
  .ribbon {
    position: absolute;
    left: 26px;
    top: 126px;
    width: 168px;
    height: 270px;
  }
  .plate-number {
    position: absolute;
    left: 224px;
    top: 130px;
    width: 640px;
    height: 200px;
  }
  .plate-number text {
    font-family: "Saira Condensed", sans-serif;
    font-weight: 400;
    font-size: 250px;
    fill: var(--ink-light);
  }
  .plate-cause {
    position: absolute;
    left: 0;
    bottom: 10px;
    width: 100%;
    text-align: center;
    font-family: "Titillium Web", sans-serif;
    font-weight: 600;
    font-size: 54px;
    color: var(--ink-light);
    margin: 0;
    line-height: 1.2;
  }
</style>
</head>
<body>
<main class="canvas">
  <section class="plate">
    <p class="plate-heading">LEARN MORE @</p>
    <div class="plate-field">
      <div class="tag tag-month">MO</div>
      <div class="tag tag-year">YR</div>
      <h1 class="state-name">California</h1>
      <span class="mount-hole"></span>

      <svg class="ribbon" viewBox="0 0 168 270" role="img" aria-label="Awareness ribbon with a green rear leg and a front leg showing palm trees against a sunset">
        <defs>
          <linearGradient id="ribbon-fill" x1="0" y1="0" x2="0.4" y2="1">
            <stop offset="0" stop-color="var(--sunset-top)"/>
            <stop offset="0.55" stop-color="var(--sunset-mid)"/>
            <stop offset="1" stop-color="var(--sunset-low)"/>
          </linearGradient>
        </defs>
        <rect x="4" y="4" width="160" height="262" rx="16" fill="url(#ribbon-fill)" opacity="0.85"/>
        <rect x="4" y="4" width="160" height="262" rx="16" fill="none" stroke="var(--ribbon-green)" stroke-width="8"/>
      </svg>

      <svg class="plate-number" viewBox="0 0 640 200">
        <text x="0" y="192" textLength="640" lengthAdjust="spacingAndGlyphs">NEWPL8</text>
      </svg>

      <p class="plate-cause">Mental Health Awareness</p>
    </div>
    <p class="plate-footer">MINDFULSTATE.ORG</p>
  </section>
</main>
</body>
</html>
```